Olive Oil Label Needs Graphic Designs

We need two sister label designs for 500ml bottles for our new brand "Casa Lumen". Casa Lumen is a high-end olive oil from Baeza, Spain which will be sold in the US. The oil will be produced from both Arbequina olives and Picual olives. Therefore, envisioning the same design just a different color scheme for the different labels.
The label should have the following characteristics; clean and simple, stand-out from mainstream labels, be eye-catching, give perception of high-end / high-quality.
Our current thinking of what we want (but please let your creative juices flow); lighter background, to be more eye catching, graphics of and olive, a olive branch or olive tree.
Text which should appear on the label are (not necessarily in this order);
Casa Lumen
Extra Virgin Olive Oil
Family Reserve
Arbequina (One design)
Picual (Second design)
The label should be about 3 inches wide and 5.5 inches in height.

```html
<!DOCTYPE html>
<html lang="en">
<head>
<meta charset="utf-8">
<title>Casa Lumen – Extra Virgin Olive Oil Labels</title>
<link rel="stylesheet" href="https://fonts.googleapis.com/css2?family=Cinzel:wght@400&family=Playfair+Display:ital,wght@0,700;1,700&family=Raleway:wght@400&display=swap">
<style>
  :root {
    --page: #ffffff;
    --cream: #f6f1d6;
    --cream-light: #fbf8e8;
    --cream-deep: #ebe3b8;
    --frame-light: #c9dc7a;
    --frame-mid: #8fb23a;
    --frame-dark: #5f8a22;
    --leaf-green: #6f9e2a;
    --leaf-dark: #3f6e1a;
    --ribbon: #1f4a26;
    --ribbon-edge: #0f2d14;
    --ribbon-text: #e9e6c6;
    --ink: #1a1a1a;
    --copy-green: #5f8d27;
  }
  html, body {
    margin: 0;
    padding: 0;
    width: 1200px;
    height: 900px;
    overflow: hidden;
    background: var(--page);
  }
  .canvas {
    position: relative;
    width: 1200px;
    height: 900px;
  }
  .label {
    position: absolute;
    width: 342px;
    height: 630px;
  }
  .label--arbequina { left: 20px; top: 148px; }
  .label--picual { left: 809px; top: 160px; }
  .label__shape {
    position: absolute;
    inset: 0;
    width: 100%;
    height: 100%;
  }
  .label__tree {
    position: absolute;
    left: 110px;
    top: 40px;
    width: 130px;
    height: 215px;
    background:
      radial-gradient(circle at 50% 20%, rgba(143,178,58,0.55) 0 30%, transparent 60%),
      linear-gradient(180deg, var(--leaf-green) 0%, var(--leaf-dark) 100%);
    border-radius: 50% 50% 12% 12% / 45% 45% 8% 8%;
    opacity: 0.85;
  }
  .label__brand {
    position: absolute;
    left: 0;
    right: 0;
    top: 282px;
    text-align: center;
    font-family: "Playfair Display", serif;
    font-weight: 700;
    font-size: 46px;
    color: var(--ink);
    margin: 0;
  }
  .label__type {
    position: absolute;
    left: 0;
    right: 0;
    top: 358px;
    text-align: center;
    font-family: "Raleway", sans-serif;
    font-size: 21px;
    color: var(--copy-green);
    margin: 0;
  }
  .label__ribbon {
    position: absolute;
    left: 48px;
    top: 404px;
    width: 260px;
    height: 58px;
  }
  .label__ribbon-text {
    position: absolute;
    left: 48px;
    top: 416px;
    width: 260px;
    text-align: center;
    font-family: "Cinzel", serif;
    font-size: 16px;
    letter-spacing: 0.5px;
    color: var(--ribbon-text);
    margin: 0;
  }
  .label__oval {
    position: absolute;
    left: 54px;
    top: 476px;
    width: 234px;
    height: 98px;
  }
  .label__variety {
    position: absolute;
    left: 54px;
    top: 505px;
    width: 234px;
    text-align: center;
    font-family: "Playfair Display", serif;
    font-style: italic;
    font-weight: 700;
    font-size: 28px;
    color: var(--ink);
    margin: 0;
  }
</style>
</head>
<body>
<main class="canvas">

  <section class="label label--arbequina" aria-label="Casa Lumen Arbequina label">
    <svg class="label__shape" viewBox="0 0 342 630" aria-hidden="true">
      <defs>
        <linearGradient id="frameA" x1="0" y1="0" x2="1" y2="1">
          <stop offset="0" stop-color="var(--frame-light)"/>
          <stop offset="0.5" stop-color="var(--frame-dark)"/>
          <stop offset="1" stop-color="var(--frame-light)"/>
        </linearGradient>
        <radialGradient id="panelA" cx="0.5" cy="0.3" r="0.8">
          <stop offset="0" stop-color="var(--cream-light)"/>
          <stop offset="0.6" stop-color="var(--cream)"/>
          <stop offset="1" stop-color="var(--cream-deep)"/>
        </radialGradient>
      </defs>
      <path d="M0 0 H342 Q316 315 342 630 H0 Q26 315 0 0 Z" fill="url(#frameA)"/>
      <path d="M14 14 H328 Q302 315 328 616 H14 Q40 315 14 14 Z" fill="url(#panelA)"/>
    </svg>
    <div class="label__tree" role="img" aria-label="Stylised olive tree illustration with round green leaves"></div>
    <h2 class="label__brand">Casa Lumen</h2>
    <p class="label__type">Extra Virgin Olive Oil</p>
    <svg class="label__ribbon" viewBox="0 0 260 58" aria-hidden="true">
      <polygon points="0,14 22,14 22,50 0,50 10,32" fill="var(--ribbon-edge)"/>
      <polygon points="260,14 238,14 238,50 260,50 250,32" fill="var(--ribbon-edge)"/>
      <path d="M12 4 Q130 -4 248 4 L248 44 Q130 36 12 44 Z" fill="var(--ribbon)"/>
    </svg>
    <p class="label__ribbon-text">FAMILY RESERVE</p>
    <svg class="label__oval" viewBox="0 0 234 98" aria-hidden="true">
      <defs>
        <linearGradient id="ovalA" x1="0" y1="0" x2="1" y2="1">
          <stop offset="0" stop-color="var(--frame-light)"/>
          <stop offset="1" stop-color="var(--frame-dark)"/>
        </linearGradient>
      </defs>
      <ellipse cx="117" cy="49" rx="113" ry="45" fill="var(--cream-light)" stroke="url(#ovalA)" stroke-width="5"/>
    </svg>
    <p class="label__variety">Arbequina</p>
  </section>

  <section class="label label--picual" aria-label="Casa Lumen Picual label">
    <svg class="label__shape" viewBox="0 0 342 630" aria-hidden="true">
      <defs>
        <linearGradient id="frameP" x1="0" y1="0" x2="1" y2="1">
          <stop offset="0" stop-color="var(--frame-light)"/>
          <stop offset="0.5" stop-color="var(--frame-dark)"/>
          <stop offset="1" stop-color="var(--frame-light)"/>
        </linearGradient>
        <radialGradient id="panelP" cx="0.5" cy="0.3" r="0.8">
          <stop offset="0" stop-color="var(--cream-light)"/>
          <stop offset="0.6" stop-color="var(--cream)"/>
          <stop offset="1" stop-color="var(--cream-deep)"/>
        </radialGradient>
      </defs>
      <path d="M0 0 H342 Q316 315 342 630 H0 Q26 315 0 0 Z" fill="url(#frameP)"/>
      <path d="M14 14 H328 Q302 315 328 616 H14 Q40 315 14 14 Z" fill="url(#panelP)"/>
    </svg>
    <div class="label__tree" role="img" aria-label="Stylised olive tree illustration with round green leaves"></div>
    <h2 class="label__brand">Casa Lumen</h2>
    <p class="label__type">Extra Virgin Olive Oil</p>
    <svg class="label__ribbon" viewBox="0 0 260 58" aria-hidden="true">
      <polygon points="0,14 22,14 22,50 0,50 10,32" fill="var(--ribbon-edge)"/>
      <polygon points="260,14 238,14 238,50 260,50 250,32" fill="var(--ribbon-edge)"/>
      <path d="M12 4 Q130 -4 248 4 L248 44 Q130 36 12 44 Z" fill="var(--ribbon)"/>
    </svg>
    <p class="label__ribbon-text">FAMILY RESERVE</p>
    <svg class="label__oval" viewBox="0 0 234 98" aria-hidden="true">
      <defs>
        <linearGradient id="ovalP" x1="0" y1="0" x2="1" y2="1">
          <stop offset="0" stop-color="var(--frame-light)"/>
          <stop offset="1" stop-color="var(--frame-dark)"/>
        </linearGradient>
      </defs>
      <ellipse cx="117" cy="49" rx="113" ry="45" fill="var(--cream-light)" stroke="url(#ovalP)" stroke-width="5"/>
    </svg>
    <p class="label__variety">Picual</p>
  </section>

</main>
</body>
</html>
```